National Sales Conference

We need a cool one page flyer inviting our sales partners to a National Sales Training Class.

Most important event in 5 years! Do not even consider missing it

Details of Sales Meeting
Nov 10th - 11th in Dallas, TX
Nov 10th (welcome party) 7-9pm

Preliminary Agenda
Nov, 10th 7-9pm Welcome Reception

Nov 11th and 12th 9-4 Tillpoint Drill Week Sales training. Learn the tools you need to become more relevant in the marketplace as we launch multiple new cutting edge products and services. Many vendors will be on hand to personally meet you and provide the tools and marketing information you need.

Location of event
Kelbrook Plaza Lodge West
2876 Harlowmere Pkwy.
Fort Worth, TX 76392
FREE Shuttle from DFW!
Updates

Please put the Brightwater Vendor Solutions logo at the TOP left and the Quillstone Remit logo make it small and near the bottom

Add the following TEXT. 

*** This event is so important our CEO, Marcus Delong has decided that we are covering all of the expenses! That's right, we will provide the sleeping room based on double occupancy, all meals, and with 10 deals in 90 days we will even reimburse your airfare if a flight is necessary. 

Be sure to include the RSVP information and lines for the to print out and check if they are coming or not as indicated in the original brief. 

This flyer will be sent to our sales agents VIA Email in PDF. Therefore, if we need to make it 2 pages so it is not so cluttered, I'm okay with that. 

Target Market(s)

Our Sales Agents

Industry/Entity Type

Training

Requirements
Must have
• One page! High energy will a strong call to action.
• Needs a small fill in the blank for an RSVP
• Name _______________
• Check Box YES! I will gladly attend. _____ # attending
• Check Box Can't make it.
• Fax RSVP to 775-319-2740 or email marcusd@brightwaterco.example

```html
<!DOCTYPE html>
<html lang="en">
<head>
<meta charset="utf-8">
<title>Invitation to the National Sales Training Class</title>
<link rel="stylesheet" href="https://fonts.googleapis.com/css2?family=Great+Vibes&family=Arimo:wght@400;700&display=swap">
<style>
  :root {
    --red: #d21f26;
    --red-deep: #a80f16;
    --white: #ffffff;
    --ink: #1b1b1b;
    --brand-blue: #1d5c8c;
    --brand-green: #6bb33f;
  }
  * { box-sizing: border-box; margin: 0; padding: 0; }
  html, body { width: 1200px; height: 2545px; overflow: hidden; background: var(--white); }
  .flyer {
    position: relative; width: 1200px; height: 2545px; overflow: hidden;
    font-family: "Arimo", Arial, sans-serif; color: var(--white); background: var(--white);
  }
  .red-field { position: absolute; left: 0; top: 0; width: 1200px; height: 2445px; }

  .brand-top {
    position: absolute; left: 30px; top: 30px; display: flex; align-items: center; gap: 14px;
    color: var(--brand-blue); font-weight: 700; font-size: 26px; line-height: 30px; width: 270px;
  }
  .brand-top .mark-square { flex: none; width: 48px; height: 48px; background: var(--brand-blue); }

  .invite-heading {
    position: absolute; left: 0; top: 0; width: 1200px; text-align: center;
    font-family: "Great Vibes", cursive; color: var(--red-deep);
  }
  .invite-heading .word { display: block; font-size: 170px; line-height: 1; padding-top: 8px; }
  .invite-heading .to-the { position: absolute; left: 680px; top: 130px; font-size: 86px; line-height: 1; }

  .title { position: absolute; left: 0; top: 318px; width: 1200px; text-align: center; line-height: 1; }
  .title .line-1 { display: block; font-weight: 700; font-size: 102px; letter-spacing: 1px; }
  .title .line-2 { display: block; font-weight: 400; font-size: 124px; margin-top: 14px; }
  .title .city { position: absolute; left: 660px; top: 262px; font-weight: 700; font-size: 60px; }

  .rule { position: absolute; left: 36px; top: 712px; width: 1130px; height: 3px; background: rgba(255,255,255,0.75); }
  .reception { position: absolute; left: 40px; top: 728px; font-size: 46px; font-weight: 400; }
  .reception strong { font-weight: 700; }
  .agenda {
    position: absolute; left: 40px; top: 798px; width: 1130px;
    font-size: 43px; font-weight: 700; line-height: 58px;
  }

  .photo {
    position: absolute; left: 0; top: 1420px; width: 1200px; height: 480px;
    background: linear-gradient(180deg, #2c3a5c 0%, #5a5f78 22%, #9a6a5a 42%, #c9a486 58%, #7d6b52 72%, #4f5d3a 86%, #3c4a2e 100%);
  }
  .venue {
    position: absolute; left: 400px; top: 1185px; width: 800px; height: 280px;
    background: var(--white); border-radius: 34px 0 0 34px; padding: 22px 0 0 56px;
    box-shadow: -6px 8px 18px rgba(0,0,0,0.3);
    color: var(--ink); transform: skewY(-2deg); transform-origin: left top;
    font-style: normal;
  }
  .venue .name { color: var(--red); font-weight: 700; font-size: 50px; line-height: 60px; }
  .venue .street, .venue .town { font-size: 60px; line-height: 66px; }
  .venue .shuttle { color: var(--red); font-weight: 700; font-size: 50px; line-height: 62px; }

  .expenses {
    position: absolute; left: 40px; top: 1925px; width: 1130px;
    font-size: 34px; font-weight: 700; line-height: 44px;
  }

  .rsvp-form { position: absolute; left: 40px; top: 2160px; width: 1130px; font-size: 36px; }
  .rsvp-form .row { display: flex; align-items: flex-end; gap: 16px; height: 62px; }
  .rsvp-form .box { flex: none; width: 36px; height: 36px; border: 4px solid var(--white); margin-bottom: 4px; }
  .rsvp-form .blank { border-bottom: 3px solid var(--white); height: 40px; margin-bottom: 6px; }
  .rsvp-form .blank.long { flex: 1; }
  .rsvp-form .blank.short { width: 140px; }
  .rsvp-form strong { font-weight: 700; }

  .rsvp {
    position: absolute; left: 0; top: 2380px; width: 1200px; text-align: center;
    font-size: 32px; font-weight: 400; white-space: nowrap;
  }
  .rsvp strong { font-weight: 700; }

  .partners {
    position: absolute; left: 0; top: 2445px; width: 1200px; height: 100px;
    display: flex; align-items: center; justify-content: center;
  }
  .partner { display: flex; align-items: center; gap: 14px; font-weight: 700; font-size: 34px; color: var(--brand-green); }
  .partner .mark-circle { width: 46px; height: 46px; border-radius: 50%; background: var(--brand-green); }
</style>
</head>
<body>
<main class="flyer">
  <svg class="red-field" viewBox="0 0 1200 2445" aria-hidden="true">
    <defs>
      <radialGradient id="redGlow" cx="0.5" cy="0.3" r="0.8">
        <stop offset="0" stop-color="#e8353a"/>
        <stop offset="0.6" stop-color="#d21f26"/>
        <stop offset="1" stop-color="#a80f16"/>
      </radialGradient>
    </defs>
    <path d="M0 250 C 300 200, 700 300, 1200 215 L1200 2445 L0 2445 Z" fill="url(#redGlow)"/>
    <path d="M0 235 C 300 185, 700 285, 1200 200" fill="none" stroke="#a80f16" stroke-width="6" opacity="0.6"/>
    <rect x="0" y="2365" width="1200" height="80" fill="#a80f16"/>
  </svg>

  <div class="brand-top"><span class="mark-square"></span>Brightwater Vendor Solutions</div>

  <header class="invite-heading">
    <span class="word">Invitation</span>
    <span class="to-the">to the</span>
  </header>

  <h1 class="title">
    <span class="line-1">NATIONAL SALES</span>
    <span class="line-2">TRAINING CLASS</span>
    <span class="city">in Dallas, TX</span>
  </h1>

  <div class="rule"></div>
  <p class="reception">Nov, 10th 7-9pm <strong>Welcome Reception</strong></p>
  <p class="agenda">Nov 11th and 12th 9-4 Tillpoint Drill Week Sales training. Learn the tools you need to become more relevant in the marketplace as we launch multiple new cutting edge products and services. Many vendors will be on hand to personally meet you and provide the tools and marketing information you need.</p>

  <div class="photo" role="img" aria-label="Photograph of the hotel building and entrance canopy at dusk"></div>

  <address class="venue">
    <div class="name">Kelbrook Plaza Lodge West</div>
    <div class="street">2876 Harlowmere Pkwy.</div>
    <div class="town">Fort Worth, TX 76392</div>
    <div class="shuttle">FREE Shuttle from DFW!</div>
  </address>

  <p class="expenses">*** This event is so important our CEO, Marcus Delong has decided that we are covering all of the expenses! That's right, we will provide the sleeping room based on double occupancy, all meals, and with 10 deals in 90 days we will even reimburse your airfare if a flight is necessary.</p>

  <form class="rsvp-form">
    <div class="row"><strong>Name</strong><span class="blank long"></span></div>
    <div class="row"><span class="box"></span><strong>YES!</strong> I will gladly attend. <span class="blank short"></span> # attending</div>
    <div class="row"><span class="box"></span>Can't make it.</div>
  </form>

  <p class="rsvp">Fax <strong>RSVP</strong> to <strong>775-319-2740</strong> or email <strong>marcusd@brightwaterco.example</strong></p>

  <footer class="partners">
    <div class="partner"><span class="mark-circle"></span>Quillstone Remit</div>
  </footer>
</main>
</body>
</html>
```